KV Media Group stationary project
don't have one
Use same font as used in my logo
logo attached
Molly Brennan
President/CEO
don't have one yet
mbrennan@kvmediagroupexample.com
www.kvmediagroupexample.com
I don't have an address yet so can you do an A & B version so I know what it will look like and can add the address at a later date. Also, as part of this contest which includes business card/letterhead/envelopes, can you also do a design for invoice and fax sheet. Thanks!

```html
<!DOCTYPE html>
<html lang="en">
<head>
<meta charset="utf-8">
<title>KV Media Group – Business Card</title>
<link href="https://fonts.googleapis.com/css2?family=Montserrat:wght@400;500;700;800&display=swap" rel="stylesheet">
<style>
  :root {
    --backdrop: #e9e6e1;
    --card-white: #ffffff;
    --ink: #2b2b2b;
    --ink-soft: #4a4a4a;
    --rule-dark: #333333;
    --orange-deep: #f39c00;
    --orange-light: #fbc33b;
    --logo-orange: #f5a000;
  }
  * { margin: 0; padding: 0; box-sizing: border-box; }
  html, body {
    width: 1200px; height: 780px; overflow: hidden;
    background: var(--backdrop);
    font-family: "Montserrat", Arial, sans-serif;
  }
  .card {
    position: absolute; left: 75px; top: 90px;
    width: 1050px; height: 600px;
    border-radius: 34px; overflow: hidden;
    background: var(--card-white);
    box-shadow: 0 12px 30px rgba(0,0,0,.18);
  }
  .card-top {
    position: absolute; left: 0; top: 0; width: 100%; height: 340px;
    display: flex; flex-direction: column; align-items: center;
  }
  .brand-mark {
    width: 112px; height: 112px; border-radius: 50%;
    background: var(--logo-orange);
    margin-top: 56px;
  }
  .brand-name {
    margin-top: 26px;
    font-weight: 800; font-size: 56px; letter-spacing: 1px;
    color: var(--ink); text-transform: uppercase; line-height: 1;
  }
  .card-rule {
    position: absolute; left: 0; top: 340px; width: 100%; height: 5px;
    background: var(--rule-dark);
  }
  .card-bottom {
    position: absolute; left: 0; top: 345px; width: 100%; height: 255px;
    background: linear-gradient(180deg, var(--orange-light) 0%, var(--orange-deep) 100%);
  }
  .person {
    position: absolute; right: 585px; top: 52px;
    text-align: right; color: var(--ink);
  }
  .person-name { font-weight: 700; font-size: 27px; line-height: 1.2; }
  .person-title { font-weight: 700; font-size: 22px; margin-top: 4px; line-height: 1.2; }
  .person-address { font-size: 20px; color: var(--ink-soft); margin-top: 12px; line-height: 1.35; white-space: nowrap; }
  .divider {
    position: absolute; left: 488px; top: 46px; width: 3px; height: 150px;
    background: var(--rule-dark);
  }
  .contacts {
    position: absolute; left: 514px; top: 46px;
    list-style: none; color: var(--ink-soft); font-size: 20px;
  }
  .contacts li { display: flex; align-items: center; gap: 12px; height: 36px; white-space: nowrap; }
  .contacts svg { width: 22px; height: 22px; flex: none; }
</style>
</head>
<body>
  <section class="card">
    <div class="card-top">
      <div class="brand-mark"></div>
      <div class="brand-name">KV Media Group</div>
    </div>
    <div class="card-rule"></div>
    <div class="card-bottom">
      <div class="person">
        <div class="person-name">Molly Brennan</div>
        <div class="person-title">President/CEO</div>
        <div class="person-address">Unit 48 Sample Avenue,<br>Region, Code 0000.Land</div>
      </div>
      <div class="divider"></div>
      <ul class="contacts">
        <li>
          <svg viewBox="0 0 24 24" aria-hidden="true"><rect x="7" y="2" width="10" height="20" rx="2" fill="#2b2b2b"/><rect x="9" y="5" width="6" height="9" fill="#fbc33b"/></svg>
          555-014-2271
        </li>
        <li>
          <svg viewBox="0 0 24 24" aria-hidden="true"><text x="12" y="18" font-size="20" font-family="Arial, sans-serif" font-weight="700" text-anchor="middle" fill="#2b2b2b">@</text></svg>
          mbrennan@kvmediagroupexample.com
        </li>
        <li>
          <svg viewBox="0 0 24 24" aria-hidden="true"><circle cx="12" cy="12" r="9" fill="none" stroke="#2b2b2b" stroke-width="2"/><ellipse cx="12" cy="12" rx="4" ry="9" fill="none" stroke="#2b2b2b" stroke-width="1.6"/><line x1="3" y1="12" x2="21" y2="12" stroke="#2b2b2b" stroke-width="1.6"/></svg>
          www.kvmediagroupexample.com
        </li>
      </ul>
    </div>
  </section>
</body>
</html>
```